Construction proffessionals servicing the inner suburbs of Melbournes NorthWest specialising in aler

I would like a web site that is sharp, contemporary and simple to navigate, ie.not too many pages. i would like a home page with some info about us, who we are what our history is and my passion for building and construction based on impeccable customer focus. i would like a projects page and somewhere for clients to add testimonials. i would like a project calculator as well so prospective clients can work out a rough budget prior to contacting. i would like the colours to be in line with my logo which i have uploaded. i have many photos which can be used and can be shared via drop box when required. I would like it to be personal to capture our transparent process. i would like to add our company process as well. be brave and take risks.

Target Market(s)

People renovating and extending their homes, people needing inspections on new homes and pre-purchase inspections

Industry/Entity Type

Construction

Number of Pages Required

5+ page

Requirements
Must have
• Professional, easy to navigate, provide viewers with a happy experience, look great, contacts, project calculator, link through to my training company www.ormwaybuilds.au also check ormwaybuilds on instagram for pics
Nice to have
• Links to instagram, fonts to match email signature

```html
<!DOCTYPE html>
<html lang="en">
<head>
<meta charset="utf-8">
<title>Ormway Builds – Building &amp; Construction Advice</title>
<link href="https://fonts.googleapis.com/css2?family=Open+Sans:ital,wght@0,400;0,600;0,700;1,400&family=Raleway:wght@600;700;800&display=swap" rel="stylesheet">
<style>
:root{
  --orange:#f39a1e;
  --orange-dark:#d9820c;
  --ink:#333;
  --muted:#8a8a8a;
  --soft:#f1f2f4;
  --cream:#f1efe9;
  --footer:#1f1f1f;
  --footer-line:#3a3a3a;
}
*{margin:0;padding:0;box-sizing:border-box}
html,body{width:1200px;height:2476px;overflow:hidden}
body{font-family:"Open Sans",Arial,sans-serif;color:var(--ink);background:#fff;font-size:15px;line-height:1.6}
h2,h3,h4{font-family:"Raleway","Open Sans",sans-serif}
.site-header{height:80px;display:flex;align-items:center;justify-content:space-between;padding:0 40px;background:#fff}
.brand{display:flex;align-items:center;gap:10px;font-family:"Raleway",sans-serif;font-weight:800;font-size:26px;color:var(--orange)}
.brand-square{width:30px;height:30px;background:var(--orange)}
.main-nav{display:flex;gap:26px;font-size:12px;font-weight:600;text-transform:uppercase;color:#555}
.main-nav a:first-child{color:var(--orange)}
.hero{position:relative;height:500px}
.hero-photo{position:absolute;inset:0;background:linear-gradient(100deg,#5b4530 0%,#8d6a48 30%,#c9b59a 55%,#e4e0da 75%,#cfd4d8 100%)}
.hero-copy{position:absolute;left:120px;top:100px;width:560px;color:#fff}
.hero-copy h1{font-family:"Raleway",sans-serif;font-size:22px;font-weight:700;letter-spacing:1px;text-transform:uppercase;white-space:nowrap}
.hero-copy p{font-size:13px;margin-top:6px;opacity:.9}
.hero-tags{margin-top:30px;font-size:14px;font-weight:700;text-transform:uppercase;letter-spacing:1px}
.hero-tags span{color:var(--orange);font-weight:400;font-style:italic;text-transform:lowercase}
.btn{display:inline-block;background:var(--orange);color:#fff;font-size:12px;font-weight:700;text-transform:uppercase;padding:12px 26px;letter-spacing:.5px}
.hero-copy .btn{margin-top:50px}
.section-title{text-align:center;font-size:28px;font-weight:700;text-transform:uppercase;letter-spacing:1px;color:#2b2b2b}
.section-sub{text-align:center;font-size:12px;color:var(--muted);margin-top:4px}
.rule{width:60px;height:3px;background:var(--orange);margin:12px auto 0}
.about{height:380px;padding-top:40px}
.about-text{width:780px;margin:24px auto 0;text-align:center;font-size:13px;color:#555}
.features{display:flex;justify-content:center;gap:60px;margin-top:40px}
.feature{width:260px;display:flex;gap:14px}
.feature svg{flex:none}
.feature h3{font-size:16px;font-weight:700;line-height:1.4}
.feature p{font-size:12px;color:var(--muted);line-height:1.5}
.who{background:var(--soft);height:500px;padding-top:40px}
.who-body{display:flex;gap:40px;margin:40px 120px 0}
.who-photo{width:580px;height:290px;background:linear-gradient(135deg,#e0a23c,#a7a9ad 55%,#55616d)}
.who-text{width:360px;font-size:13px;color:#555}
.who-text p+p{margin-top:14px}
.read-more{color:var(--orange);font-weight:600;font-size:12px}
.projects{height:420px;padding-top:36px}
.project-grid{display:flex;justify-content:center;gap:40px;margin-top:32px}
.project{width:320px}
.project-photo{position:relative;height:200px}
.project-photo .plus{position:absolute;right:0;bottom:0;width:34px;height:34px;background:var(--orange);color:#fff;font-size:24px;line-height:34px;text-align:center}
.p1{background:linear-gradient(180deg,#a9c3dc,#c06b4e 70%,#7d8a69)}
.p2{background:linear-gradient(180deg,#2c3038,#5c636d 60%,#8b7a63)}
.p3{background:linear-gradient(180deg,#b7cde0,#b3674a 60%,#7b5a4c)}
.project-meta{text-align:center;margin-top:8px}
.project-meta small{display:block;font-size:10px;color:var(--muted);letter-spacing:1px;text-transform:uppercase}
.project-meta h4{font-size:16px;font-weight:700;text-transform:uppercase;letter-spacing:1px;line-height:1.4}
.testimonials{background:var(--cream);height:320px;padding-top:36px}
.quote{width:700px;margin:28px auto 0;text-align:center;font-style:italic;font-size:14px;color:#555}
.client{text-align:center;margin-top:22px}
.client-avatar{width:60px;height:60px;border-radius:50%;background:#b8b3a8;margin:0 auto}
.client-name{font-size:13px;font-weight:600;margin-top:6px;text-decoration:underline}
.site-footer{background:var(--footer);height:276px;color:#bbb;position:relative}
.footer-cols{display:flex;gap:40px;padding:36px 60px 0 80px}
.footer-col{width:240px;font-size:12px;line-height:1.9}
.footer-col h4{color:#fff;font-size:12px;font-weight:700;text-transform:uppercase;letter-spacing:1px;margin-bottom:12px}
.footer-input{width:190px;height:30px;background:var(--orange);margin-top:4px;color:#fff;padding:0 10px;line-height:30px}
.footer-col .btn{margin-top:10px;padding:7px 18px;font-size:10px}
.socials{display:flex;gap:8px;margin-top:10px}
.socials span{width:24px;height:24px;border-radius:50%;background:#3a8fd6}
.footer-bottom{position:absolute;left:0;right:0;bottom:0;height:40px;border-top:1px solid var(--footer-line);padding:12px 80px;font-size:11px;color:#888}
</style>
</head>
<body>
<header class="site-header">
  <div class="brand"><span class="brand-square"></span>Ormway</div>
  <nav class="main-nav"><a>Home</a><a>About us</a><a>Our Philosophy</a><a>Testimonials</a><a>Project</a><a>Contact</a></nav>
</header>

<section class="hero">
  <div class="hero-photo" role="img" aria-label="Builders in hard hats and safety vests reviewing plans on a timber-framed construction site"></div>
  <div class="hero-copy">
    <h1>Providing quality expert advice</h1>
    <p>Ormway Builds. Renovation specialists, professional advice</p>
    <div class="hero-tags">Inspection <span>or</span> Mediation</div>
    <a class="btn">Request a quote &gt;</a>
  </div>
</section>

<section class="about">
  <h2 class="section-title">About us</h2>
  <p class="section-sub">Duis aute irure dolor in reprehenderit in voluptate velit esse</p>
  <div class="rule"></div>
  <p class="about-text">Darren Holt – Operations Manager and business principal. Darren's experience in the industry is vast and covers all areas of light commercial, medium density and residential construction and he has been elevated from all sides of the complex arena that is the building industry.</p>
  <div class="features">
    <div class="feature">
      <svg width="34" height="34" viewBox="0 0 34 34"><circle cx="17" cy="11" r="6" fill="#555"/><path d="M5 32c0-8 5-12 12-12s12 4 12 12z" fill="#555"/></svg>
      <div><h3>Expert Advice</h3><p>Sed ut perspiciatis unde omnis iste natus error sit voluptatem</p></div>
    </div>
    <div class="feature">
      <svg width="34" height="34" viewBox="0 0 34 34"><path d="M3 17 17 5l14 12" fill="none" stroke="#555" stroke-width="3"/><rect x="8" y="16" width="18" height="15" fill="#555"/></svg>
      <div><h3>New Home Quality Inspection</h3><p>Sed ut perspiciatis unde omnis iste natus error sit voluptatem</p></div>
    </div>
    <div class="feature">
      <svg width="34" height="34" viewBox="0 0 34 34"><path d="M17 3v28M6 9h22M6 9l-4 10h8zM28 9l-4 10h8z" fill="none" stroke="#555" stroke-width="2.5"/></svg>
      <div><h3>Dispute Resolution</h3><p>Sed ut perspiciatis unde omnis iste natus error sit voluptatem</p></div>
    </div>
  </div>
</section>

<section class="who">
  <h2 class="section-title">Who we are</h2>
  <p class="section-sub">Do you need building advice, or simple someone to help you through the minefield of the building industry?</p>
  <div class="rule"></div>
  <div class="who-body">
    <div class="who-photo" role="img" aria-label="Three builders in hard hats and hi-vis vests looking at a tablet on site"></div>
    <div class="who-text">
      <p>If you answered yes to any of these questions or to help you, Ormway Builds Pty Ltd was created in 2016 to assist people with the issues that confront consumers, owner builders, landlords, purchasers and builders in these modern, technical and more litigious times. Ormway Builds has worked with its clients to keep building disputes out of the legal system and to settle them fairly and efficiently.</p>
      <p>Ormway Builds Pty Ltd is a family business that understands the pressures associated with the industry. Through Darren, there are over 30 years of experience in the building and construction industry as a tradesman.</p>
      <p class="read-more">Read more &gt;</p>
    </div>
  </div>
</section>

<section class="projects">
  <h2 class="section-title">Our latest projects</h2>
  <p class="section-sub">Duis aute irure dolor in reprehenderit in voluptate velit esse</p>
  <div class="rule"></div>
  <div class="project-grid">
    <div class="project"><div class="project-photo p1" role="img" aria-label="Brick family home with tiled roof after renovation"><span class="plus">+</span></div><div class="project-meta"><small>Excepteur</small><h4>Duis aute irure</h4></div></div>
    <div class="project"><div class="project-photo p2" role="img" aria-label="Modern living room interior of a completed extension"><span class="plus">+</span></div><div class="project-meta"><small>Excepteur</small><h4>Duis aute irure</h4></div></div>
    <div class="project"><div class="project-photo p3" role="img" aria-label="Two-storey brick townhouses under a blue sky"><span class="plus">+</span></div><div class="project-meta"><small>Excepteur</small><h4>Duis aute irure</h4></div></div>
  </div>
</section>

<section class="testimonials">
  <h2 class="section-title">What our client say about us</h2>
  <div class="rule"></div>
  <p class="quote">" Sed ut perspiciatis unde omnis iste natus error sit voluptatem accusantium doloremque laudantium, totam rem aperiam, eaque ipsa quae ab illo, inventore veritatis "</p>
  <div class="client"><div class="client-avatar" role="img" aria-label="Client portrait"></div><p class="client-name">Thomas Jones</p></div>
</section>

<footer class="site-footer">
  <div class="footer-cols">
    <div class="footer-col"><h4>Quick links</h4>Home<br>About us<br>Our philosophy<br>Testimonials<br>Project<br>Contact</div>
    <div class="footer-col"><h4>Our philosophy</h4>Duis aute irure dolor in reprehenderit in voluptate velit esse cillum dolore eu fugiat nulla pariatur. Excepteur sint occaecat cupidatat non proident, sunt in culpa.</div>
    <div class="footer-col"><h4>Subscribe newsletter</h4><div class="footer-input">Your email address</div><a class="btn">Subscribe</a></div>
    <div class="footer-col"><h4>We are here</h4>14 Alder Lane, Brunswick West<br>VIC 3055, Australia<br>(03) 9000 4172<br>hello@ormwaybuilds.au<br>www.ormwaybuilds.au<div class="socials"><span></span><span></span><span></span></div></div>
  </div>
  <div class="footer-bottom">© 2016 – Kestrel Trade Pathways</div>
</footer>
</body>
</html>
```